Training Course Info Brochure

Hi there, I'm looking for a design for A4 Flyer (2-3 pages) on our new Course - Infection Control. I have included a previous brochure on our courses so the designed can see the look and feel we are looking for.

As this is about Infection Control, I would also like to see some RED in the design or wording.

The brochure will need to include quite a few industry/ government logos as well and graphics are important. I have included some (Health Care Industry workers) and am also open to other graphics.

Thanks for considering!

Target Market(s)

The Health profession and students wanting to work in the health field

Industry/Entity Type

Health Care

Font styles to use
Sans Serif

Colors
3277b5
f78f20
ffffff
ec1f27

Requirements
Must have
• Similar feel to the brochure I have included in this brief.

SOME RED lettering as we are teaching Infection Control during the COVID19 pandemic
Nice to have
• Lovely design with quite a few photos graphics

Company details:

Carrow Academy of Learning
RTO 73648
FREECALL : 1800 437 982
www.carrowlearning.edu.au
info@carrowlearning.edu.au

```html
<!DOCTYPE html>
<html lang="en">
<head>
<meta charset="utf-8">
<title>Infection Control Skill Set – Course Brochure</title>
<link href="https://fonts.googleapis.com/css2?family=Saira+Semi+Condensed:wght@300;400;600;700&family=Open+Sans:wght@400;600;700&display=swap" rel="stylesheet">
<style>
:root{
  --red:#e31e2b;
  --red-dark:#c8161f;
  --navy:#163a6b;
  --blue:#3277b5;
  --blue-deep:#1f4f8a;
  --orange:#f78f20;
  --white:#ffffff;
  --ink:#2b2b2b;
  --grey-panel:#eef0f3;
  --stage:#3a3b3f;
  --head:"Saira Semi Condensed","Arial Narrow",sans-serif;
  --body:"Open Sans",sans-serif;
}
*{box-sizing:border-box;margin:0;padding:0}
html,body{width:1200px;height:568px;overflow:hidden;background:var(--stage)}
.stage{position:relative;width:1200px;height:568px}
.page{position:absolute;top:53px;width:329px;height:466px;background:var(--white);overflow:hidden;font-family:var(--body);color:var(--ink)}
.page--cover{left:73px}
.page--about{left:437px}
.page--audience{left:801px}
.top-rule{position:absolute;left:0;right:0;top:13px;height:3px;background:var(--orange)}
.page-tab{position:absolute;right:0;top:0;width:26px;height:13px;background:#e4e4e4;clip-path:polygon(18% 0,100% 0,100% 100%,0 100%);font:600 6px/13px var(--body);color:#777;text-align:center;padding-left:4px}
.photo{position:absolute}
/* footer */
.footer{position:absolute;left:0;right:0;bottom:0;height:19px;background:var(--orange);display:flex;align-items:center;font:700 5.6px/1 var(--body);color:var(--white)}
.footer__rto{height:100%;width:50px;flex:none;background:var(--navy);clip-path:polygon(0 0,100% 0,88% 100%,0 100%);display:flex;align-items:center;padding-left:7px;font-size:6px}
.footer__items{display:flex;gap:6px;padding-left:4px;white-space:nowrap}
.footer__items span{display:flex;align-items:center;gap:2px}
.footer svg{width:6px;height:6px}
/* cover */
.cover-head{position:absolute;left:0;right:0;top:16px;height:63px;background:var(--red);padding:11px 0 0 11px;color:var(--white)}
.cover-head__title{font:700 17.5px/1 var(--head);display:inline-block;border-bottom:1px solid var(--white);padding-bottom:1px;white-space:nowrap}
.cover-head__sub{font:300 14.5px/1.15 var(--head);margin-top:3px;white-space:nowrap}
.cover-band{position:absolute;left:0;right:0;top:259px;height:14px;background:var(--red)}
.seal{position:absolute;left:246px;top:190px;width:75px;height:75px;border-radius:50%;background:var(--white);border:3px solid var(--red);box-shadow:0 0 0 2px var(--white)}
.unit-code{position:absolute;left:10px;top:279px;font:700 16px/1 var(--head);color:var(--red-dark)}
.unit-title{position:absolute;left:11px;top:296px;font:600 9px/1 var(--head);color:var(--red-dark);white-space:nowrap}
.brand{position:absolute;left:13px;top:352px;width:106px;display:flex;align-items:center;gap:5px;font:700 8px/1.15 var(--body);color:var(--navy)}
.brand__mark{width:14px;height:14px;flex:none;background:var(--navy)}
.cost{position:absolute;left:132px;top:320px;width:185px;height:106px;border:1.2px solid var(--red);padding:3px;text-align:center}
.cost__head{background:var(--navy);color:var(--white);font:700 15px/21px var(--head);height:21px}
.cost__free{font:700 18px/1 var(--head);color:var(--red);margin-top:13px}
.cost__line{font:400 8.6px/1.3 var(--head);color:#333;white-space:nowrap}
.cost__rule{height:1px;background:var(--red);margin:4px 2px 4px}
.cost__alt{font:400 9px/1 var(--head);color:#333;white-space:nowrap}
.cost__alt b{color:var(--red);font-weight:700}
/* about */
.about-panel{position:absolute;left:0;right:0;top:79px;height:179px;background:linear-gradient(180deg,var(--blue) 0%,var(--blue-deep) 100%)}
.about-title{position:absolute;left:0;right:0;top:84px;text-align:center;font:700 16px/1 var(--head);color:var(--white);padding-left:22px}
.shield{position:absolute;left:11px;top:47px;width:52px;height:52px;border-radius:50%;background:var(--red);border:3px solid var(--white)}
.about-box{position:absolute;left:11px;top:108px;width:307px;height:141px;background:var(--white);border-radius:5px;padding:10px 8px 0 8px}
.about-box::before{content:"";position:absolute;left:146px;top:-6px;border:6px solid transparent;border-top:0;border-bottom-color:var(--white)}
.about-box__head{font:700 6.4px/1 var(--head);color:var(--red);margin-bottom:6px;white-space:nowrap}
.dots{list-style:none}
.dots li{position:relative;padding-left:6px;font-size:5.1px;line-height:1.38;margin-bottom:3px;color:#333}
.dots li::before{content:"";position:absolute;left:0;top:2px;width:3px;height:3px;border-radius:50%;background:var(--red)}
.dots em{font-style:normal;color:var(--red)}
.format{position:absolute;left:6px;top:270px;width:152px}
.sec-head{font:700 7px/1 var(--head);color:var(--red);white-space:nowrap}
.sec-sub{font:700 4.8px/1.2 var(--body);color:var(--red);margin:2px 0 3px;white-space:nowrap}
.format .dots li{font-size:4.9px;margin-bottom:1px;line-height:1.35}
.gain{position:absolute;left:165px;top:263px;width:157px;height:173px;border:1px solid var(--red);background:var(--grey-panel);padding:3px}
.gain__head{position:relative;background:var(--red);color:var(--white);text-align:center;font:700 12px/21px var(--head);height:21px}
.gain__head::after{content:"";position:absolute;left:72px;bottom:-5px;border:5px solid transparent;border-bottom:0;border-top-color:var(--red)}
.ticks{list-style:none;margin-top:18px;padding:0 2px 0 5px}
.ticks li{display:flex;gap:3px;font:400 6.5px/1.22 var(--head);color:#333}
.ticks svg{flex:none;width:7px;height:7px;margin-top:1px}
.gain__base{position:absolute;left:-1px;right:-1px;bottom:-1px;height:6px;background:var(--red)}
/* audience */
.who{position:absolute;left:6px;top:16px;width:149px;height:53px;background:var(--red);color:var(--white);text-align:center;font:700 11.5px/1.12 var(--head);padding-top:5px}
.who::after{content:"";position:absolute;left:69px;bottom:-5px;border:5px solid transparent;border-bottom:0;border-top-color:var(--red);z-index:2}
.who-panel{position:absolute;left:6px;top:188px;width:149px;height:199px;background:linear-gradient(180deg,var(--blue) 0%,var(--blue-deep) 100%);color:var(--white);padding:10px 10px 0 11px;font-size:5.3px;line-height:1.38}
.who-panel p{margin-bottom:6px}
.who-panel ul{list-style:none}
.who-panel li{position:relative;padding-left:5px;margin-bottom:.5px}
.who-panel li::before{content:"";position:absolute;left:0;top:2.6px;width:2px;height:2px;background:var(--white)}
.who-panel__base{position:absolute;left:0;right:0;bottom:0;height:9px;background:var(--red)}
.icon-disc{position:absolute;left:224px;top:20px;width:36px;height:36px;border-radius:50%;background:var(--blue);border:2px solid var(--white);box-shadow:0 0 0 1.5px var(--blue);display:flex;align-items:center;justify-content:center}
.pathways{position:absolute;left:168px;top:59px;width:152px;font-size:5.2px;line-height:1.38;color:#444}
.pathways__head{font:700 7px/1 var(--head);color:var(--navy);margin-bottom:9px;white-space:nowrap}
.pathways p{margin-bottom:5px}
.pathways ul{list-style:none;font-size:4.9px;line-height:1.3;margin-bottom:5px}
.pathways li{position:relative;padding-left:5px}
.pathways li::before{content:"";position:absolute;left:0;top:2.3px;width:2px;height:2px;background:#444}
.url-pill{position:absolute;left:163px;top:242px;width:157px;height:11px;border-radius:6px;background:var(--blue);color:var(--white);font:700 5.3px/11px var(--body);text-align:center}
.brand--small{left:238px;top:280px;width:70px;font-size:6px;gap:3px}
.brand--small .brand__mark{width:10px;height:10px}
.recog{position:absolute;left:165px;top:336px;width:152px;font-size:5.2px;line-height:1.38;color:#444}
.recog h3{font:700 7.6px/1 var(--head);color:var(--red);margin-bottom:3px}
.partners{position:absolute;left:5px;top:391px;width:316px;height:46px;border:1px solid var(--red);display:flex;align-items:center;justify-content:space-around;padding:0 8px}
.partners i{display:block;background:#d7dbe2}
</style>
</head>
<body>
<main class="stage">

  <section class="page page--cover">
    <div class="top-rule"></div>
    <header class="cover-head">
      <h1 class="cover-head__title">INFECTION CONTROL SKILL SET</h1>
      <p class="cover-head__sub">HLTSS00064 for Health Care Workers</p>
    </header>
    <div class="photo" style="left:0;top:79px;width:329px;height:180px;background:linear-gradient(120deg,#5d6470 0%,#9aa3b0 45%,#6f7783 100%)" role="img" aria-label="Health care worker in surgical cap, mask, safety glasses and blue gloves, with red virus particles floating beside her"></div>
    <div class="cover-band"></div>
    <div class="seal" role="img" aria-label="Course seal"></div>
    <h2 class="unit-code">HLTINF001</h2>
    <p class="unit-title">Comply with infection prevention, control policies and procedures</p>
    <div class="brand"><span class="brand__mark"></span><span>Carrow Academy of Learning</span></div>
    <div class="cost">
      <div class="cost__head">COURSE COST</div>
      <div class="cost__free">FREE</div>
      <div class="cost__line">infection control skill sets</div>
      <div class="cost__line">for everyone in Western Australia or</div>
      <div class="cost__rule"></div>
      <div class="cost__alt"><b>$350/</b> for students outside of WA</div>
    </div>
    <footer class="footer">
      <div class="footer__rto">RTO 73648</div>
      <div class="footer__items">
        <span><svg viewBox="0 0 10 10"><path d="M2 1l2 2-1 1.5c.6 1.2 1.4 2 2.5 2.5L7 6l2 2-1.5 1.5C4.5 9 1 5.5.5 2.5z" fill="#fff"/></svg>FREECALL:1800 437 982</span>
        <span><svg viewBox="0 0 10 10"><rect x="1" y="2" width="8" height="6" fill="none" stroke="#fff"/><path d="M1 2l4 3 4-3" fill="none" stroke="#fff"/></svg>info@carrowlearning.edu.au</span>
        <span><svg viewBox="0 0 10 10"><circle cx="5" cy="5" r="4" fill="none" stroke="#fff"/><path d="M1 5h8M5 1c-2 2.5-2 5.5 0 8M5 1c2 2.5 2 5.5 0 8" fill="none" stroke="#fff" stroke-width=".7"/></svg>www.carrowlearning.edu.au</span>
      </div>
    </footer>
  </section>

  <section class="page page--about">
    <div class="top-rule"></div>
    <div class="page-tab">p2</div>
    <div class="photo" style="left:0;top:16px;width:329px;height:63px;background:linear-gradient(90deg,#9aa4b5 0%,#d6d9df 50%,#b9a08e 100%)" role="img" aria-label="Carer smiling with an elderly woman in an aged care setting"></div>
    <div class="about-panel"></div>
    <div class="shield">
      <svg viewBox="0 0 46 46" width="46" height="46"><path d="M23 8l12 4v9c0 8-5 13-12 16-7-3-12-8-12-16v-9z" fill="none" stroke="#fff" stroke-width="2.6"/><path d="M17 22l5 5 8-9" fill="none" stroke="#fff" stroke-width="3"/></svg>
    </div>
    <h2 class="about-title">ABOUT THIS COURSE</h2>
    <div class="about-box">
      <h3 class="about-box__head">PROTECT YOURSELF AND OTHERS IN THE COMMUNITY FROM INFECTIOUS DISEASES</h3>
      <ul class="dots">
        <li>There is not better time than now, to formally Upskill yourself and your team with a Nationally Accredited unit of Competency in Infection Control prevention <em>including the latest COVID19 infection control protocols</em> (Health Authority). Fast track your skills with Carrow's Accredited Infection Control Skill set to get you job ready or enhance your current workplace skills.</li>
        <li>The COVID19 pandemic has highlighted the important of building the capacity and understanding of the workforce to <em>practice safe infection control procedures.</em></li>
        <li>This skill set will provide you with the skills and knowledge to assist in protecting yourself and others in the community from infectious diseases.</li>
        <li>You will understand how infections are spread, ways of preventing the spread of infection and how to protect yourself and others from infection.</li>
        <li>The skill set is becoming increasingly important for all Health Care Workers – and all workers are encouraged to upskill themselves today, whether you are becoming Job Ready or for your professional development in Industry.</li>
      </ul>
    </div>
    <div class="format">
      <h3 class="sec-head">COURSE FORMAT</h3>
      <p class="sec-sub">Online with face-to-face tutorial (in person or via MeetLink)</p>
      <ul class="dots">
        <li>Our course is delivered to you online which allows you to undertaken study at your own pace. It's recomended completion occurs within a month.</li>
        <li>If you have completed the Online Component of your course, you are invited into a Practical Lab Session via face to face learning; to practice skills and undertake a workplace simulated activity.</li>
        <li>Regional locations may be fulfilled by MeetLink technology and Carrow may also conduct on-site visits as required. Carrow also travel to regional locations throughout the year. Group training sessions are also available for corporates and workplaces.</li>
      </ul>
      <h3 class="sec-head" style="margin:8px 0 4px">MENTOR SUPPORT &amp; PRACTICAL SESSIONS</h3>
      <ul class="dots">
        <li>Students are welcomed to the course by a short induction by your Tutor/Mentor to start you on your way with confidence!</li>
        <li>All of Carrow's student resources, learner materials, videos are contained in Carrow's easy to use LMS and learning is provided online at your convenience.</li>
      </ul>
    </div>
    <div class="gain">
      <div class="gain__head">GAIN THIS SKILLS</div>
      <ul class="ticks">
        <li><svg viewBox="0 0 10 10"><circle cx="5" cy="5" r="4" fill="none" stroke="#e31e2b"/><path d="M3 5l2 2 4-5" fill="none" stroke="#e31e2b" stroke-width="1.2"/></svg>Gain Industry Certification in Hand Hygiene</li>
        <li><svg viewBox="0 0 10 10"><circle cx="5" cy="5" r="4" fill="none" stroke="#e31e2b"/><path d="M3 5l2 2 4-5" fill="none" stroke="#e31e2b" stroke-width="1.2"/></svg>Gain Industry Certification in COVID19 Infection Control</li>
        <li><svg viewBox="0 0 10 10"><circle cx="5" cy="5" r="4" fill="none" stroke="#e31e2b"/><path d="M3 5l2 2 4-5" fill="none" stroke="#e31e2b" stroke-width="1.2"/></svg>Gain Industry Certification in Cleaning, Disinfection and Sterilisation</li>
        <li><svg viewBox="0 0 10 10"><circle cx="5" cy="5" r="4" fill="none" stroke="#e31e2b"/><path d="M3 5l2 2 4-5" fill="none" stroke="#e31e2b" stroke-width="1.2"/></svg>Using personal protective equipment safely (practical session with complimentary PPE samples)</li>
        <li><svg viewBox="0 0 10 10"><circle cx="5" cy="5" r="4" fill="none" stroke="#e31e2b"/><path d="M3 5l2 2 4-5" fill="none" stroke="#e31e2b" stroke-width="1.2"/></svg>Understanding the chain of infection</li>
        <li><svg viewBox="0 0 10 10"><circle cx="5" cy="5" r="4" fill="none" stroke="#e31e2b"/><path d="M3 5l2 2 4-5" fill="none" stroke="#e31e2b" stroke-width="1.2"/></svg>Identify infection hazards and assess risks</li>
        <li><svg viewBox="0 0 10 10"><circle cx="5" cy="5" r="4" fill="none" stroke="#e31e2b"/><path d="M3 5l2 2 4-5" fill="none" stroke="#e31e2b" stroke-width="1.2"/></svg>How to prevent the spread and transmission of infection</li>
        <li><svg viewBox="0 0 10 10"><circle cx="5" cy="5" r="4" fill="none" stroke="#e31e2b"/><path d="M3 5l2 2 4-5" fill="none" stroke="#e31e2b" stroke-width="1.2"/></svg>Maintaining a clean work environment</li>
      </ul>
      <div class="gain__base"></div>
    </div>
    <footer class="footer">
      <div class="footer__rto">RTO 73648</div>
      <div class="footer__items">
        <span><svg viewBox="0 0 10 10"><path d="M2 1l2 2-1 1.5c.6 1.2 1.4 2 2.5 2.5L7 6l2 2-1.5 1.5C4.5 9 1 5.5.5 2.5z" fill="#fff"/></svg>FREECALL:1800 437 982</span>
        <span><svg viewBox="0 0 10 10"><rect x="1" y="2" width="8" height="6" fill="none" stroke="#fff"/><path d="M1 2l4 3 4-3" fill="none" stroke="#fff"/></svg>info@carrowlearning.edu.au</span>
        <span><svg viewBox="0 0 10 10"><circle cx="5" cy="5" r="4" fill="none" stroke="#fff"/><path d="M1 5h8M5 1c-2 2.5-2 5.5 0 8M5 1c2 2.5 2 5.5 0 8" fill="none" stroke="#fff" stroke-width=".7"/></svg>www.carrowlearning.edu.au</span>
      </div>
    </footer>
  </section>

  <section class="page page--audience">
    <div class="top-rule"></div>
    <div class="page-tab">p3</div>
    <h2 class="who">WHO IS<br>THIS COURSE IS<br>IDEAL FOR?</h2>
    <div class="photo" style="left:6px;top:69px;width:149px;height:119px;background:linear-gradient(135deg,#e9eef3 0%,#c7d3df 60%,#9fb2c6 100%)" role="img" aria-label="Smiling nurse holding a blue folder in a dental clinic"></div>
    <div class="who-panel">
      <p>The skill set course is most suitable for anyone working the healthcare sector, or those looking to enter employment in the health fields.</p>
      <p>This training is for care workers across all health care settings, including:</p>
      <ul>
        <li>Hospitals</li>
        <li>Primary care</li>
        <li>Medical practices, allied health, GP and specialist clinics</li>
        <li>Aged care (both in residential aged care facilities or with visiting carers at home, including cleaners and cooks)</li>
        <li>Disability (both in residential/shared care facilities or part-time carers in people's homes, including cleaners and cooks)</li>
        <li>Allied health</li>
        <li>Aboriginal Community Controlled Health Services</li>
        <li>Pharmacies</li>
        <li>Dental practices, including dentists, nurses, cleaners and receptionists</li>
      </ul>
      <div class="who-panel__base"></div>
    </div>
    <div class="icon-disc">
      <svg viewBox="0 0 20 20" width="17" height="17"><rect x="2" y="6" width="16" height="11" rx="1.5" fill="none" stroke="#fff" stroke-width="1.6"/><path d="M7 6V4h6v2M2 11h16" fill="none" stroke="#fff" stroke-width="1.6"/></svg>
    </div>
    <div class="pathways">
      <h3 class="pathways__head">JOB OPPORTUNITIES &amp; STUDY PATHWAYS</h3>
      <p>This course does not lead to a specific job outcome but will be helpful if you are, or would like to work in any of the areas described above.<br>Our training course is designed to make students Job Ready or to enhance their job role.</p>
      <p>The Units of Competency is a recognised Unit that can be used as a Credit Transfer in Qualifications such as :</p>
      <ul>
        <li>Certificate III Business Administration (Medical)</li>
        <li>Cert III and IV Health Administration</li>
        <li>Cert III in Individual Support (Aging, disability, home and community)</li>
        <li>Cert III in Allied Health Assistance</li>
        <li>Cert III/IV Dental Assisting</li>
        <li>Certificate III in Aboriginal and/or Torres Strait Islander Primary Health Care</li>
        <li>Cert II/III Community Services</li>
        <li>Certificate III in Cleaning Operations</li>
        <li>Cert II and III Health Support Services</li>
      </ul>
      <p>More Qualifications that include this Unit of Competency can be found at</p>
    </div>
    <div class="url-pill">https://unitfinder.edu.au/Details/HLTINF001</div>
    <div class="photo" style="left:171px;top:264px;width:65px;height:60px;background:linear-gradient(135deg,#1d2a36 0%,#2f6f7c 60%,#6fc2c8 100%)" role="img" aria-label="Dark teal microscope view of a coronavirus particle"></div>
    <div class="brand brand--small"><span class="brand__mark"></span><span>Carrow Academy of Learning</span></div>
    <div class="recog">
      <h3>INDUSTRY RECOGNIZED</h3>
      <p>Carrow's unique program in Infection Control is supported by leading Industry bodies, and includes certification by the Health Authority &amp; other leading Health bodies in Australia. Our Unit of competency is Australian Recognised and Accredited.</p>
    </div>
    <div class="partners" aria-label="Partner and accreditation badges">
      <i style="width:36px;height:22px"></i>
      <i style="width:30px;height:26px;border-radius:50%"></i>
      <i style="width:34px;height:18px"></i>
      <i style="width:32px;height:26px"></i>
      <i style="width:28px;height:26px"></i>
      <i style="width:54px;height:22px;background:#fbe3c4"></i>
    </div>
    <footer class="footer">
      <div class="footer__rto">RTO 73648</div>
      <div class="footer__items">
        <span><svg viewBox="0 0 10 10"><path d="M2 1l2 2-1 1.5c.6 1.2 1.4 2 2.5 2.5L7 6l2 2-1.5 1.5C4.5 9 1 5.5.5 2.5z" fill="#fff"/></svg>FREECALL:1800 437 982</span>
        <span><svg viewBox="0 0 10 10"><rect x="1" y="2" width="8" height="6" fill="none" stroke="#fff"/><path d="M1 2l4 3 4-3" fill="none" stroke="#fff"/></svg>info@carrowlearning.edu.au</span>
        <span><svg viewBox="0 0 10 10"><circle cx="5" cy="5" r="4" fill="none" stroke="#fff"/><path d="M1 5h8M5 1c-2 2.5-2 5.5 0 8M5 1c2 2.5 2 5.5 0 8" fill="none" stroke="#fff" stroke-width=".7"/></svg>www.carrowlearning.edu.au</span>
      </div>
    </footer>
  </section>

</main>
</body>
</html>
```